Veterinary Hospital Brochure - 2 Drafts - 1 Normal and 1 Fun.

Meadowbrook Pet Hospital needs a brochure to promote our veterinary hospital. These will be delivered to local mailboxes. I would like to see atleast 2 submissions from each designer.
One submission conservative and A4 folded DL and another submission more radical and interesting with innovative folding or crazy concepts. Maybe the brochure could be designed to fold into a dog house ?
I want at least one version to be VERY SIMPLE AND INTIMATE.
Our existing website is here: http://furlane.example/ and our new website will look like this: http://trial4.pagemint.example/#home
Please use colors and images from the new website, and information from the old website. The heading font used in the new site is Qorvatype - Otter Tilt Sketchline
I want the brochure to be simple and engaging on first view, and then provide the opportunity to find more information if desired. The brochure needs to be captivating on the outside so people don't throw it away immediately.

We will soon need letterhead, flags, pens, business cards, signs and vouchers so there is the opportunity for more work for the successful designer.

Target Market(s)

Women 25 to 44

Industry/Entity Type

Veterinary

Contact Information for Business Card

Meadowbrook Pet Hospital
14 Marlow Crescent
Tamsworth Vale
NSW 2417
Phone: 02 61938205
Emergency: 0417360592
Fax: 02 83159462
www.meadowbrookvets.example
contact@meadowbrookvets.example

Font styles to use
Script

Requirements
Must have
• Colors from the new website: http://meadowbrookvets.example/ and new logo.
• Information from the old website: http://furlane.example/
• 2 drafts - A normal A4 folded DL flyer and an interesting crazy design.
Nice to have
• VERY SIMPLE
• Subdued
• Intimate
Should not have
• Intense colours
• Red

```html
<!DOCTYPE html>
<html lang="en">
<head>
<meta charset="utf-8">
<title>Meadowbrook Pet Hospital – Trifold Brochure</title>
<link href="https://fonts.googleapis.com/css2?family=Yellowtail&family=Open+Sans:wght@400;600;700&display=swap" rel="stylesheet">
<style>
  :root{
    --page:#e6e6e4;
    --green:#9acb3f;
    --green-deep:#5f8a22;
    --white:#ffffff;
    --ink:#4a3b2c;
    --ink-soft:#6d6156;
    --orange:#ef8a3c;
    --brown:#4b3222;
  }
  *{box-sizing:border-box;margin:0;padding:0}
  html,body{width:917px;height:1200px;overflow:hidden;background:var(--page)}
  body{position:relative;font-family:"Open Sans",Arial,sans-serif;color:var(--ink)}
  .sheet{position:absolute;left:40px;width:837px;height:550px;background:var(--white);box-shadow:0 4px 12px rgba(0,0,0,.25);overflow:hidden}
  .sheet--outside{top:35px}
  .sheet--inside{top:615px}
  .panel{position:absolute;top:0;width:279px;height:550px}
  .panel--1{left:0}.panel--2{left:279px}.panel--3{left:558px}
  .green{background:var(--green);color:var(--white)}
  .photo{position:absolute;left:0;width:100%;z-index:0}
  .script{font-family:"Yellowtail",cursive;font-weight:400;line-height:1}
  .copy{font-size:7.6px;line-height:1.45}
  .copy p{margin-bottom:6px}
  .copy b{font-style:italic;font-weight:700}
  .brand{display:flex;align-items:center;gap:8px;justify-content:center;font-family:"Open Sans",Arial,sans-serif;font-weight:700;color:var(--brown);font-size:17px;letter-spacing:.5px;line-height:1.15;text-align:left}
  .brand__mark{width:14px;height:14px;background:var(--orange);flex:none}

  /* outside */
  .about{position:absolute;top:200px;left:0;width:279px;height:170px;padding:16px 20px 0 22px}
  .about h2{font-size:22px;margin-bottom:8px;white-space:nowrap}
  .map{position:absolute;top:40px;left:36px;width:206px;height:186px;border:4px solid var(--orange);background:linear-gradient(135deg,#eef0ea,#dcdfd6)}
  .contact{position:absolute;top:255px;left:52px;width:215px}
  .contact h2{font-size:24px;margin-bottom:12px}
  .contact ul{list-style:none}
  .contact li{display:flex;align-items:center;gap:14px;font-size:7.6px;height:21px;white-space:nowrap}
  .contact svg{width:10px;height:10px;flex:none;fill:#6a8f2e}
  .panel--2 .brand{position:absolute;top:478px;left:0;width:100%;color:var(--brown)}
  .cover-brand{position:absolute;top:58px;left:0;width:100%}
  .cover-title{position:absolute;top:150px;left:40px;color:var(--green);font-size:56px;transform:rotate(-8deg);line-height:.9;white-space:nowrap;z-index:2}
  .cover-title span{display:block;padding-left:6px}
  .cover-sub{position:absolute;top:268px;right:22px;width:136px;font-size:10.5px;line-height:1.3;color:var(--ink-soft);z-index:2}

  /* inside */
  .headline{color:var(--green-deep);font-size:24px;line-height:.95}
  .nail{position:absolute;top:178px;left:28px;width:228px}
  .nail .copy{margin-top:12px}
  .surgery{position:absolute;top:410px;left:28px;width:228px}
  .surgery .headline{display:inline-block}
  .icon-box{position:absolute;top:6px;right:18px;width:36px;height:26px;background:var(--green-deep)}
  .surgery .copy{margin-top:12px}
  .block{position:absolute;left:30px;width:230px}
  .block h2{font-size:24px;margin-bottom:8px;white-space:nowrap}
  .meds{position:absolute;top:470px;left:30px;width:230px}
  .meds h2{font-size:22px;line-height:.9;display:inline-block}
  .meds .box{position:absolute;top:4px;right:10px;width:26px;height:20px;background:var(--white)}
  .services{position:absolute;top:200px;left:28px;width:230px}
  .services h2{font-size:23px;margin-bottom:10px}
  .services h3{font-family:"Yellowtail",cursive;font-weight:400;font-size:22px;margin:22px 0 8px}
  .ticks{list-style:none}
  .ticks li{display:flex;align-items:center;gap:10px;font-size:7.8px;height:21.5px}
  .ticks svg{width:10px;height:10px;flex:none;stroke:var(--white);stroke-width:2.4;fill:none}
</style>
</head>
<body>

<!-- Outside of brochure -->
<section class="sheet sheet--outside">
  <div class="panel panel--1 green">
    <div class="photo" style="top:0;height:200px;background:linear-gradient(160deg,#c8cfd4,#8fa7a9 55%,#6c8486)" role="img" aria-label="Veterinary surgeon in scrubs and mask preparing for surgery"></div>
    <div class="about">
      <h2 class="script">Meadowbrook Pet Hospital</h2>
      <div class="copy">
        <p>Is a companion animal Veterinary Hospital in Tamsworth Vale NSW. We treat Dogs, Cats, Reptiles, Rodents, Birds, and other little critters.</p>
        <p>As a companion animal only Hospital, we are dedicated to improving the wellbeing of your beloved pets.</p>
        <p>We think they are part of the family and should receive the absolute best possible care.</p>
      </div>
    </div>
    <div class="photo" style="top:370px;height:180px;background:linear-gradient(120deg,#a08a6e,#d8c7ab 50%,#8b7559)" role="img" aria-label="Woman at a table stroking a tabby cat"></div>
  </div>

  <div class="panel panel--2 green">
    <div class="map" role="img" aria-label="Street map showing the hospital location"></div>
    <div class="contact">
      <h2 class="script">Contact Us</h2>
      <ul>
        <li><svg viewBox="0 0 10 10"><path d="M5 0.5 0 5h1.5v4.5h2.5V6.5h2v3h2.5V5H10z"/></svg>14 Marlow Crescent, Tamsworth Vale, NSW 2417</li>
        <li><svg viewBox="0 0 10 10"><path d="M2.2 0.5 4 2.8 3 4a6 6 0 0 0 3 3l1.2-1 2.3 1.8L8.5 9.5C4.5 9.5 .5 5.5 .5 1.5z"/></svg>(02) 6193 8205 or 6193MPET</li>
        <li><svg viewBox="0 0 10 10"><path d="M2.5 0.5h5v2.5h-5zM0.5 3.5h9v4h-2v2h-5v-2h-2zM3.5 6.5v2h3v-2z"/></svg>(02) 8315 9462</li>
        <li><svg viewBox="0 0 10 10"><path d="M0.5 2h9v6h-9zM1 2.5 5 5.5 9 2.5v1L5 6.5 1 3.5z"/></svg>contact@meadowbrookvets.example</li>
        <li><svg viewBox="0 0 10 10"><circle cx="5" cy="5" r="4.5"/></svg>www.meadowbrookvets.example</li>
      </ul>
    </div>
    <div class="brand"><span class="brand__mark"></span>MEADOWBROOK<br>PET HOSPITAL</div>
  </div>

  <div class="panel panel--3">
    <div class="brand cover-brand"><span class="brand__mark"></span>MEADOWBROOK<br>PET HOSPITAL</div>
    <h1 class="script cover-title">Caring<span>For Pets</span></h1>
    <p class="cover-sub">A companion animal Veterinary Hospital in Tamsworth Vale, NSW</p>
    <div class="photo" style="top:315px;height:235px;background:linear-gradient(180deg,#ffffff 0%,#d9c49d 16%,#a57d4d 60%,#5a4331)" role="img" aria-label="Woman hugging her dog"></div>
  </div>
</section>

<!-- Inside of brochure -->
<section class="sheet sheet--inside">
  <div class="panel panel--1">
    <div class="photo" style="top:0;height:165px;background:linear-gradient(110deg,#c79e7a,#e8dccd 50%,#a48466)" role="img" aria-label="Two vet nurses caring for a large dog"></div>
    <div class="nail">
      <h2 class="script headline">Complimentary<br>Nail Clipping</h2>
      <div class="copy">
        <p><b>Meadowbrook Pet Hospital</b> provides free nail clipping. All we ask is a note donation to Helper Hounds Trust.</p>
        <p><b>Meadowbrook Pet Hospital</b> is built on the grounds of a chapel built in 1897. The chapel hall has been converted into a beautiful reception area.</p>
        <p>We have constructed a modern veterinary hospital with small animal surgical facilities, X-ray, ultrasound, dog and cat wards, laboratory, isolation, multiple consultation rooms and a huge treatment area. Come in for a tour of our facility or go online at furlane.example</p>
      </div>
    </div>
    <div class="surgery">
      <h2 class="script headline">Companion<br>Animal Surgery</h2>
      <span class="icon-box"></span>
      <div class="copy"><p><b>Meadowbrook Pet Hospital</b> has the latest surgical instrumentation and anaesthetic monitoring to ensure the success of surgery and outcomes for your pets.</p></div>
    </div>
  </div>

  <div class="panel panel--2 green">
    <div class="block" style="top:38px">
      <h2 class="script">Puppy Classes</h2>
      <div class="copy">
        <p><b>Meadowbrook Pet Hospital</b> runs a 5 week puppy class. These are great fun and provide essential socialization and training for you and your puppy.</p>
        <p>The classes prevent a range of behavioral issues and are an essential part of our prevention is better than cure philosophy.</p>
      </div>
    </div>
    <div class="block" style="top:172px">
      <h2 class="script">Qualified Caring Team</h2>
      <div class="copy"><p><b>Meadowbrook Pet Hospital</b> friendly, qualified and caring team help families and their pets. We want to make sure your pet is as healthy and happy as they can be by creating a comfortable and inviting environment where you feel part of our family and receive ongoing support.</p></div>
    </div>
    <div class="photo" style="top:280px;left:0;width:265px;height:172px;background:linear-gradient(100deg,#cdb79a,#efe3cf 45%,#b98d5f)" role="img" aria-label="Puppy giving a high five to a woman"></div>
    <div class="meds">
      <h2 class="script">Companion Animal<br>Medecine</h2>
      <span class="box"></span>
      <div class="copy" style="margin-top:8px"><p>Our diagnostic facilities enable us to identify disease rapidly and treat promptly with the correct therapies.</p></div>
    </div>
  </div>

  <div class="panel panel--3 green">
    <div class="photo" style="top:0;height:185px;background:linear-gradient(130deg,#5f4a3b,#b7845a 50%,#6e5646)" role="img" aria-label="Ginger cat lying on the floor"></div>
    <div class="services">
      <h2 class="script">Our Services</h2>
      <div class="copy"><p><b>Meadowbrook Pet Hospital</b> provides gold standard pet health care. This means we offer you the best possible care and remind you when it is due.</p></div>
      <h3>This Includes:</h3>
      <ul class="ticks">
        <li><svg viewBox="0 0 10 10"><path d="M1 5.5 4 8.5 9 1.5"/></svg>Vaccination</li>
        <li><svg viewBox="0 0 10 10"><path d="M1 5.5 4 8.5 9 1.5"/></svg>Desexing</li>
        <li><svg viewBox="0 0 10 10"><path d="M1 5.5 4 8.5 9 1.5"/></svg>Heartworm Prevention</li>
        <li><svg viewBox="0 0 10 10"><path d="M1 5.5 4 8.5 9 1.5"/></svg>Flea Prevention</li>
        <li><svg viewBox="0 0 10 10"><path d="M1 5.5 4 8.5 9 1.5"/></svg>Microchipping</li>
        <li><svg viewBox="0 0 10 10"><path d="M1 5.5 4 8.5 9 1.5"/></svg>Intestinal Worming</li>
        <li><svg viewBox="0 0 10 10"><path d="M1 5.5 4 8.5 9 1.5"/></svg>Dental Care</li>
        <li><svg viewBox="0 0 10 10"><path d="M1 5.5 4 8.5 9 1.5"/></svg>Premium Food</li>
      </ul>
    </div>
  </div>
</section>

</body>
</html>
```